Website for peer to peer car sharing service

Hi all,

We need a web design for a new environmental friendly peer-to-peer car sharing website.

The website will serve as a marketplace where car owners can list their car and drivers that who do not have access to a car can rent a suitable car. It is important for us to emphasis that this is a community where the main purpose is to use the vehicles on the street in a more efficient way.

Attached are five pictures where we have sketched up the five main pages:

File 1. Info site for a particular car.
File 2. Logo.
File 3. Register a car.
File 4. Sign up.
File 5. Search.
File 6. Front page.

The logo for the company is attached (File 2) and it would be ideal to design the website in relation to the logo. The final design should relate to a secure market place which is environmental friendly.

We would like this webpage to be in the same spirit as www.velnoro.it, www.brundale.com, www.plimtrovesite.com, https://wend.kul.net, https://garbelow.com etc.

We look forward to see your designs.

Best regards,
The Trundo Team.

Hi guys, 

Please take :

1) Could you please design icons for for  'FAQ' and 'Insurance' in the header, locate the icons right to the Trundo logo. We only want two icons ('FAQ' and 'Insurance')  right to the Trundo logo.

2) The height of the header should be the same as the header of faplex.com

3) The price tags for the cars (below the top section) should be similar to the price tags at mostanbee.com.

4) We would like you to start to design the other pages (the sub-pages listed in the project description:
a)Info site for a particular car.
b)Register a car. 
c)Search results (similar to http://www.pevrotank.com/find-car).

Please take a look at the picture attached for the sub-pages:

https://files.quenmolt.example/brief_uploads/000001_3_search_000001_brief000001.jpg

https://files.quenmolt.example/brief_uploads/000002_4_infositeforaparticularcar_000002_brief000002.jpg

http://www.quenmolt.example/file.aspx?fileLocation=storage_url/brief_uploads/000003_5_registeracar_brief000003.jpg

Best regards, 
Trundo team 

Target Market(s)

The target market are people from 20-40 years old who are environmental friendly, also tourists who visit the city and would like to rent a car.

Industry/Entity Type

It Company

Requirements
Must have
• It is required that the designer that will be chosen will hand in layered PSD files of each web page.

```html
<!DOCTYPE html>
<html lang="en">
<head>
<meta charset="utf-8">
<title>Trundo – Peer to peer car sharing</title>
<link href="https://fonts.googleapis.com/css2?family=Bebas+Neue&family=Open+Sans:wght@400;600;700&display=swap" rel="stylesheet">
<style>
:root{
  --black:#050505;
  --green:#7dc242;
  --green-dark:#5fa52c;
  --page:#f3f3f3;
  --card:#ffffff;
  --line:#e2e2e2;
  --ink:#222222;
  --text:#6b6b6b;
  --muted:#9a9a9a;
  --footer-text:#d8d8d8;
}
*{margin:0;padding:0;box-sizing:border-box}
html,body{width:1200px;height:2400px;overflow:hidden}
body{position:relative;background:var(--page);font-family:"Open Sans",Arial,sans-serif;color:var(--text)}

/* header */
.site-header{position:absolute;left:0;top:0;width:1200px;height:145px;background:var(--black)}
.brand{position:absolute;left:104px;top:52px;display:flex;align-items:center;gap:12px}
.brand-dot{width:34px;height:34px;border-radius:50%;background:var(--green)}
.brand-name{font-weight:700;font-size:38px;color:#fff;line-height:1}
.search{position:absolute;left:517px;top:26px;width:256px;height:27px;background:#2a2a2a;border-radius:2px;font-size:10px;color:#cfcfcf;padding:6px 10px}
.search svg{position:absolute;right:9px;top:8px}
.list-car{position:absolute;left:816px;top:29px;font-size:13px;color:#e6e6e6}
.account{position:absolute;left:965px;top:30px;font-size:12px;font-weight:700;color:#fff}
.account .login{color:var(--green)}
.account .sep{color:#777;margin:0 8px}
.main-nav{position:absolute;left:517px;top:64px;display:flex}
.main-nav a{font-family:"Bebas Neue",sans-serif;font-size:26px;color:#fff;text-decoration:none;margin-right:27px;letter-spacing:.3px}
.main-nav a:last-child{margin-right:0}
.main-nav a.active{color:var(--green)}

/* hero */
.hero{position:absolute;left:0;top:145px;width:1200px;height:519px;
  background:radial-gradient(ellipse at 35% 55%,#5c5f66 0%,#2d3038 40%,#12151b 100%)}
.hero-photo{position:absolute;inset:0;background:linear-gradient(180deg,rgba(180,195,215,.35) 0%,rgba(40,44,52,0) 45%,rgba(120,120,125,.35) 100%)}
.hero-panel{position:absolute;left:632px;top:127px;width:448px;height:224px;background:rgba(25,25,25,.72);padding:18px 14px}
.hero-panel h1{font-family:"Bebas Neue",sans-serif;font-weight:400;font-size:44px;color:#fff;line-height:1}
.hero-panel p{font-size:17px;color:#e2e2e2;margin-top:6px}
.hero-input{margin-top:12px;width:420px;height:40px;background:rgba(60,60,60,.8);color:#ddd;font-size:16px;padding:9px 10px}
.btn{display:inline-block;background:var(--green);color:#fff;font-size:15px}
.hero-panel .btn{margin-top:12px;padding:8px 16px}
.slider-arrow{position:absolute;top:216px;width:50px;height:50px;border-radius:50%;background:#fff}
.slider-arrow svg{position:absolute;left:15px;top:14px}

/* car cards */
.car-card{position:absolute;top:712px;width:323px;height:341px;background:var(--card);border:1px solid var(--line)}
.car-photo{height:229px}
.price-tag{position:absolute;left:3px;top:139px;width:102px;height:55px;background:var(--green);color:#fff;padding:4px 11px}
.price-tag small{display:block;font-size:13px;line-height:1.2}
.price-tag b{font-weight:400;font-size:19px;line-height:1.1}
.owner{position:absolute;left:11px;top:250px;display:flex;align-items:center;gap:16px}
.owner-photo{width:91px;height:80px;background:linear-gradient(#cfd6dd,#8d8f93)}
.owner-name{font-size:14px;color:#444}
.owner-city{font-size:13px;color:#888}

/* article panels */
.panel{position:absolute;background:var(--card);border:1px solid var(--line)}
.panel h2{font-family:"Bebas Neue",sans-serif;font-weight:400;font-size:24px;color:var(--ink);letter-spacing:.3px;line-height:1}
.panel .sub{font-size:13.5px;color:#555;margin-top:4px}
.panel .date{font-size:13.5px;font-weight:700;color:#222;margin-top:8px}
.panel .body{font-size:13.3px;line-height:25px;color:var(--text);margin-top:10px;text-align:justify}

.video{position:absolute;left:588px;top:47px;width:365px;height:208px;background:linear-gradient(180deg,#9fb3c2 0%,#4f6170 45%,#20262d 100%)}
.video .play{position:absolute;left:163px;top:75px}
.video-bar{position:absolute;left:0;bottom:0;width:100%;height:22px;background:#1b1b1b}
.video-bar i{position:absolute;left:22px;top:9px;width:260px;height:4px;background:#3d3d3d}
.video-bar i:before{content:"";position:absolute;left:0;top:0;width:110px;height:4px;background:#5aa5d8}

/* insurance */
.insurance-art{position:absolute;left:26px;top:18px;width:160px;height:108px;background:radial-gradient(ellipse at 50% 60%,#b5cc3c 0%,#8aa52a 55%,#fff 72%)}
.insurance h3{position:absolute;left:224px;top:22px;font-weight:400;font-size:31px;color:var(--green)}
.insurance p{position:absolute;left:226px;top:68px;width:580px;font-size:13.5px;line-height:23px;color:var(--text)}
.insurance .btn{position:absolute;left:855px;top:50px;width:104px;height:39px;text-align:center;line-height:39px;font-size:14px}

/* social widget */
.widget{position:absolute;left:682px;top:35px;width:309px;height:293px;background:#fff;border:1px solid #dcdcdc}
.widget-head{height:28px;background:#eceef3;font-size:12px;font-weight:700;color:#333;padding:6px 8px;position:relative}
.widget-like{position:absolute;right:34px;top:6px;width:42px;height:17px;background:#dfe3ea;border:1px solid #b7bfcc}
.widget-count{position:absolute;right:4px;top:6px;width:28px;height:17px;border:1px solid #ccc;background:#fff;font-size:11px;font-weight:400;text-align:center;line-height:15px}
.widget-banner{height:64px;background:#000;display:flex;align-items:center;gap:8px;padding-left:22px}
.widget-banner .brand-dot{width:20px;height:20px}
.widget-banner span{font-weight:700;font-size:19px;color:#fff}
.widget-fans{font-size:11px;color:#333;padding:6px 8px 4px}
.fan-grid{display:grid;grid-template-columns:repeat(5,51px);gap:6px 6px;padding:0 8px}
.fan i{display:block;width:51px;height:50px;background:linear-gradient(#b7a796,#5f5d5b)}
.fan span{display:block;font-size:9.5px;color:#666;text-align:center;margin-top:2px}
.widget-foot{position:absolute;left:8px;bottom:8px;font-size:10px;color:#4b5c8a;display:flex;align-items:center;gap:5px}
.widget-foot i{width:12px;height:12px;background:#4b5c8a}

/* press */
.press{position:absolute;left:100px;top:1939px;width:968px;height:56px;display:flex;align-items:center;justify-content:space-between}
.press span{font-weight:700;font-size:26px;color:#4a4a4a;letter-spacing:-.5px}
.press span.light{color:#8b8b8b}

/* footer */
.site-footer{position:absolute;left:0;top:2035px;width:1200px;height:365px;background:var(--black)}
.site-footer h4{position:absolute;top:34px;font-weight:400;font-size:17px;color:var(--green)}
.foot-list{position:absolute;top:77px;list-style:none;font-size:13.5px;line-height:25px;color:var(--footer-text)}
.newsletter p{position:absolute;left:398px;top:75px;width:233px;font-size:13.5px;line-height:21px;color:var(--footer-text);text-align:justify}
.field{position:absolute;left:398px;width:238px;height:29px;background:#fff;font-size:11px;color:#b3b3b3;padding:6px 13px}
.subscribe{position:absolute;left:528px;top:216px;width:102px;height:26px;border-radius:13px;background:var(--green);color:#000;font-size:14px;text-align:center;line-height:26px}
.connect{position:absolute;left:688px;top:82px;list-style:none;font-size:13.5px;line-height:39px;color:var(--footer-text)}
.contact-icons{position:absolute;left:814px;top:78px}
.contact-icons i{display:block;width:27px;height:27px;border-radius:50%;background:#fff;margin-bottom:12px}
.contact-info{position:absolute;left:864px;top:74px;font-size:13.5px;line-height:24.5px;color:var(--footer-text)}
.footer-brand{position:absolute;left:870px;top:227px;display:flex;align-items:center;gap:10px}
.footer-brand .brand-dot{width:26px;height:26px}
.footer-brand span{font-weight:700;font-size:30px;color:#fff}
.copyright{position:absolute;left:0;top:310px;width:1200px;text-align:center;font-size:13px;color:var(--footer-text)}
</style>
</head>
<body>

<header class="site-header">
  <div class="brand"><span class="brand-dot"></span><span class="brand-name">Trundo</span></div>
  <div class="search">Type search
    <svg width="10" height="10" viewBox="0 0 10 10"><circle cx="4" cy="4" r="3" fill="none" stroke="#bbb" stroke-width="1.4"/><line x1="6.2" y1="6.2" x2="9.3" y2="9.3" stroke="#bbb" stroke-width="1.4"/></svg>
  </div>
  <div class="list-car">List Your Cars</div>
  <div class="account"><span class="login">LOGIN</span><span class="sep">|</span>SIGN UP</div>
  <nav class="main-nav">
    <a class="active">HOME</a><a>ABOUT US</a><a>SERVICES</a><a>CARS</a><a>TESTIMONIALS</a><a>CONTACT US</a>
  </nav>
</header>

<section class="hero">
  <div class="hero-photo" role="img" aria-label="Dark grey sports sedan driving through a city street with tall towers and light trails"></div>
  <div class="slider-arrow" style="left:47px"><svg width="20" height="22" viewBox="0 0 20 22"><path d="M13 3 L5 11 L13 19" fill="none" stroke="#222" stroke-width="4"/></svg></div>
  <div class="slider-arrow" style="left:1103px"><svg width="20" height="22" viewBox="0 0 20 22"><path d="M6 3 L14 11 L6 19" fill="none" stroke="#222" stroke-width="4"/></svg></div>
  <div class="hero-panel">
    <h1>LOREM IPSUM DOLOR</h1>
    <p>Sit amet consectetur adipisicing elit sed do</p>
    <div class="hero-input">Type Here ....</div>
    <div class="btn">Find The Car</div>
  </div>
</section>

<article class="car-card" style="left:104px">
  <div class="car-photo" role="img" aria-label="Dark convertible on a coastal mountain road" style="background:linear-gradient(180deg,#6f9fd0 0%,#b9cfe0 40%,#5b6d55 62%,#3c3c3c 100%)"></div>
  <div class="price-tag"><small>Price</small><b>$25,000</b></div>
  <div class="owner"><div class="owner-photo" role="img" aria-label="Portrait of the car owner"></div><div><div class="owner-name">Dorian Pell</div><div class="owner-city">London</div></div></div>
</article>
<article class="car-card" style="left:440px">
  <div class="car-photo" role="img" aria-label="Red muscle car parked on a road at dusk" style="background:linear-gradient(180deg,#6b7d93 0%,#d2dbe2 40%,#9b2a2a 60%,#2d2d2d 100%)"></div>
  <div class="price-tag"><small>Price</small><b>$25,000</b></div>
  <div class="owner"><div class="owner-photo" role="img" aria-label="Portrait of the car owner"></div><div><div class="owner-name">Dorian Pell</div><div class="owner-city">London</div></div></div>
</article>
<article class="car-card" style="left:774px">
  <div class="car-photo" role="img" aria-label="Blue sedan in front of a city skyline at sunset" style="background:linear-gradient(180deg,#4b4c55 0%,#a58d72 40%,#2e5c9a 65%,#1c1c1f 100%)"></div>
  <div class="price-tag"><small>Price</small><b>$25,000</b></div>
  <div class="owner"><div class="owner-photo" role="img" aria-label="Portrait of the car owner"></div><div><div class="owner-name">Dorian Pell</div><div class="owner-city">London</div></div></div>
</article>

<section class="panel" style="left:104px;top:1069px;width:992px;height:296px;padding:40px 0 0 28px">
  <div style="width:530px">
    <h2>SEDUT PERSPICIATIS UNDE OMNIS ISTE NATUS ERROR SIT VOLUPTATEM</h2>
    <div class="sub">Nemo enim ipsam voluptatem quia voluptas sit aspernatur</div>
    <div class="date">May 2013 ,22nd</div>
    <p class="body">Totam rem aperiam, eaque ipsa quae ab illo inventore veritatis et quasi architecto beatae vitae dicta sunt explicabo. Nemo enim ipsam voluptatem quia voluptas sit aspernatur aut odit aut fugit, sed quia consequuntur magni dolores eos qui ratione voluptatem sequi nesciunt. Neque porro quisquam est, qui dolorem ipsum quia dolor sit amet, consectetur, adipisci velit, sed quia non numquam eius modi tempora incidunt ut labore et dolore magnam aliquam quaerat voluptatem.</p>
  </div>
  <div class="video" role="img" aria-label="Video still of a dark coupe on a waterfront at dusk">
    <svg class="play" width="36" height="36" viewBox="0 0 36 36"><path d="M10 6 L30 18 L10 30 Z" fill="#fff"/></svg>
    <div class="video-bar"><i></i></div>
  </div>
</section>

<section class="panel insurance" style="left:104px;top:1384px;width:992px;height:144px">
  <div class="insurance-art" role="img" aria-label="Cartoon green car holding an insurance document"></div>
  <h3>Your Car is fully covered with insurance</h3>
  <p>Totam rem aperiam, eaque ipsa quae ab illo inventore veritatis et quasi architecto beatae vitae dicta sunt explicabo. Nemo enim ipsam voluptatem .</p>
  <div class="btn">Read More</div>
</section>

<section class="panel" style="left:94px;top:1544px;width:991px;height:347px;padding:36px 0 0 37px">
  <div style="width:630px">
    <h2>IPSUM QUIA DOLOR SIT AMET, CONSECTETUR, ADIPISCI VELIT, SED QUIA</h2>
    <div class="sub">Nemo enim ipsam voluptatem quia voluptas sit aspernatur</div>
    <div class="date">May 2013 ,22nd</div>
    <p class="body">Totam rem aperiam, eaque ipsa quae ab illo inventore veritatis et quasi architecto beatae vitae dicta sunt explicabo. Nemo enim ipsam voluptatem quia voluptas sit aspernatur aut odit aut fugit, sed quia consequuntur magni dolores eos qui ratione voluptatem sequi nesciunt. Neque porro quisquam est, qui dolorem ipsum quia dolor sit amet, consectetur, adipisci velit, sed quia non numquam eius modi tempora incidunt ut labore et dolore magnam aliquam quaerat voluptatem.Totam rem aperiam, eaque ipsa quae ab illo inventore veritatis et quasi architecto beatae vitae dicta sunt explicabo. Nemo enim ipsam voluptatem .Totam rem aperiam, eaque ipsa quae ab illo inventore veritatis et quasi architecto .</p>
  </div>
  <aside class="widget">
    <div class="widget-head">Find us on Plazabook<span class="widget-like"></span><span class="widget-count">395</span></div>
    <div class="widget-banner"><span class="brand-dot"></span><span>Trundo</span></div>
    <div class="widget-fans">2,911 people like Oatfield Creamery</div>
    <div class="fan-grid">
      <div class="fan"><i role="img" aria-label="Member photo"></i><span>Arlo</span></div>
      <div class="fan"><i role="img" aria-label="Member photo"></i><span>Bren</span></div>
      <div class="fan"><i role="img" aria-label="Member photo"></i><span>Cyril</span></div>
      <div class="fan"><i role="img" aria-label="Member photo"></i><span>dalia</span></div>
      <div class="fan"><i role="img" aria-label="Member photo"></i><span>Elowen</span></div>
      <div class="fan"><i role="img" aria-label="Member photo"></i><span>Fen</span></div>
      <div class="fan"><i role="img" aria-label="Member photo"></i><span>Gus</span></div>
      <div class="fan"><i role="img" aria-label="Member photo"></i><span>Halvard</span></div>
      <div class="fan"><i role="img" aria-label="Member photo"></i><span>Ivo</span></div>
      <div class="fan"><i role="img" aria-label="Member photo"></i><span>Jory</span></div>
    </div>
    <div class="widget-foot"><i></i>Plazabook social plugin</div>
  </aside>
</section>

<div class="press">
  <span class="light">the wardenpost</span>
  <span>The Harbor Times</span>
  <span>The Daily Lantern</span>
  <span>Meridian Chronicle</span>
</div>

<footer class="site-footer">
  <h4 style="left:104px">Quick Links</h4>
  <ul class="foot-list" style="left:104px"><li>Home</li><li>About Us</li><li>Services</li><li>Service Plans</li><li>News</li><li>FAQ &amp; Wiki</li><li>Contact Us</li></ul>
  <h4 style="left:230px">Support Links</h4>
  <ul class="foot-list" style="left:230px"><li>Legal Notice</li><li>Privacy Policy</li><li>Terms &amp; Conditions</li><li>Help</li></ul>
  <div class="newsletter">
    <h4 style="left:398px">Newsletter SignUp</h4>
    <p>Sign-up for our daily emails by entering your information below:</p>
    <div class="field" style="top:128px">Name</div>
    <div class="field" style="top:171px">Enter Your E-Mail ID</div>
    <div class="subscribe">Subscribe</div>
  </div>
  <h4 style="left:688px">Connect With Us</h4>
  <ul class="connect"><li>Chirply</li><li>Plazabook</li><li>Linkwell</li></ul>
  <h4 style="left:856px">Contact Us</h4>
  <div class="contact-icons"><i></i><i></i><i></i></div>
  <div class="contact-info">Location :Harwick<br>Contact Info : Trundo<br>No: 48/17 ,Bellmere Arcade<br>Fenwold ,North Reach<br>Phone : 1-555-014-2271</div>
  <div class="footer-brand"><span class="brand-dot"></span><span>Trundo</span></div>
  <div class="copyright">Copyright ©2013 Company Name &nbsp;- All rights reserved</div>
</footer>

</body>
</html>
```